Velmora Cosmetics & Designer Jewellery Business Card

I'm an Independent Distributor for Velmora Cosmetics (a direct sales company) which supplies Skin care, anti-ageing, makeup, body care, hair care, Fenwick Naturals, therapeutic, fragrance, sun care and mens skin care. Also supplying Velmora Designer Jewellery.

I'm looking for a classy, elegant business card design, something simple but fresh, with soft colours (nothing hot pink or floral). I like gold or silver embossing if that's possible.

Target Market(s)

All ages and genders but predominantly 25+ females

Industry/Entity Type

Hair

Contact Information for Business Card

Tobin Carlyle
Independent Distributor - Velmora Cosmetics & Velmora Designer Jewellery
Ph: 0483 259 470
Email: tobin@quorvel.org
Product Info & Online Orders: www.velmoracosmetics-example.com.au/tobincarlyle

Requirements
Must have
• Both the Velmora Cosmetics and Velmora Designer Jewellery logos - any suitable combination of the attached files. I also have the Velmora Cosmetics logos in mono if required.
Also must include: Distributor ID 384752

```html
<!DOCTYPE html>
<html lang="en">
<head>
<meta charset="utf-8">
<title>Velmora Cosmetics – Distributor Business Card</title>
<link href="https://fonts.googleapis.com/css2?family=Cinzel:wght@500&family=Josefin+Sans:wght@300&family=Oswald:wght@400;500&display=swap" rel="stylesheet">
<style>
  :root {
    --page: #e3dfda;
    --ink: #120d0c;
    --umber: #5e4038;
    --mauve: #7d5a55;
    --copper: #9c6a4c;
    --gold: #d9a24a;
    --gold-soft: #e7c07a;
    --cream: #f3e6cf;
  }
  * { margin: 0; padding: 0; box-sizing: border-box; }
  html, body { width: 849px; height: 1200px; overflow: hidden; }
  body { background: var(--page); position: relative; }

  .card {
    position: absolute;
    left: 44px;
    width: 760px;
    height: 434px;
    overflow: hidden;
    box-shadow: 0 14px 30px rgba(40, 28, 20, .25);
  }
  .card--intro { top: 120px; }
  .card--contact { top: 646px; }
  .card__art { position: absolute; inset: 0; width: 100%; height: 100%; display: block; }

  .brand {
    position: absolute;
    display: flex;
    align-items: center;
    gap: 12px;
    white-space: nowrap;
  }
  .brand__mark {
    flex: none;
    border-radius: 50%;
    border: 2px solid var(--gold-soft);
  }
  .brand__name {
    font-family: "Cinzel", serif;
    font-weight: 500;
    color: var(--gold-soft);
    letter-spacing: 1px;
    line-height: 1;
  }
  .brand--cosmetics .brand__mark { width: 38px; height: 38px; }
  .brand--cosmetics .brand__name { font-size: 34px; }
  .brand--jewellery { gap: 9px; }
  .brand--jewellery .brand__mark { width: 20px; height: 20px; }
  .brand--jewellery .brand__name { font-size: 19px; }

  .brand__tagline {
    position: absolute;
    font-family: "Josefin Sans", sans-serif;
    font-weight: 300;
    color: var(--cream);
    font-size: 19px;
    letter-spacing: .5px;
    white-space: nowrap;
  }

  .card--intro .brand--cosmetics { left: 118px; top: 96px; }
  .card--intro .brand--jewellery { left: 350px; top: 246px; }
  .card--contact .brand__tagline { left: 176px; top: 62px; }
  .card--contact .brand--cosmetics { left: 126px; top: 94px; }
  .card--contact .brand--jewellery { left: 354px; top: 300px; }

  .role {
    position: absolute;
    font-family: "Oswald", sans-serif;
    font-weight: 500;
    text-transform: uppercase;
    color: var(--cream);
    font-size: 15px;
    letter-spacing: 1.2px;
    white-space: nowrap;
  }
  .card--intro .role { left: 350px; top: 168px; }
  .card--contact .role { left: 354px; top: 162px; }

  .contact-list {
    position: absolute;
    left: 354px; top: 196px;
    list-style: none;
    font-family: "Oswald", sans-serif;
    font-weight: 400;
    color: var(--cream);
    font-size: 15px;
    letter-spacing: 1px;
    white-space: nowrap;
  }
  .contact-list li { display: flex; align-items: center; gap: 10px; height: 26px; }
  .contact-list svg { width: 18px; height: 18px; flex: none; }

  .icon-row {
    position: absolute; left: 350px; top: 200px;
    display: flex; gap: 8px;
  }
  .icon-row svg { width: 18px; height: 18px; }

  .side-line {
    position: absolute;
    left: 26px; bottom: 26px;
    transform-origin: left bottom;
    transform: rotate(-90deg) translateY(100%);
    font-family: "Oswald", sans-serif;
    font-weight: 400;
    color: var(--cream);
    font-size: 11.5px;
    letter-spacing: 1px;
    text-transform: uppercase;
    white-space: nowrap;
    line-height: 1.5;
  }
</style>
</head>
<body>

<svg width="0" height="0" style="position:absolute" aria-hidden="true">
  <defs>
    <linearGradient id="base" x1="0" y1="0" x2="1" y2="1">
      <stop offset="0" stop-color="#6f4f4a"/>
      <stop offset=".55" stop-color="#7d5a55"/>
      <stop offset="1" stop-color="#93603f"/>
    </linearGradient>
    <linearGradient id="band" x1="0" y1="0" x2="1" y2="0">
      <stop offset="0" stop-color="#d9a24a" stop-opacity=".85"/>
      <stop offset="1" stop-color="#b9793c" stop-opacity=".85"/>
    </linearGradient>
    <linearGradient id="haze" x1="0" y1="0" x2="1" y2="1">
      <stop offset="0" stop-color="#f3e6cf" stop-opacity=".35"/>
      <stop offset="1" stop-color="#f3e6cf" stop-opacity="0"/>
    </linearGradient>
    <radialGradient id="ink" cx=".2" cy=".1" r=".9">
      <stop offset="0" stop-color="#0c0807"/>
      <stop offset=".7" stop-color="#1a1211"/>
      <stop offset="1" stop-color="#1a1211" stop-opacity="0"/>
    </radialGradient>
    <linearGradient id="strands" x1="0" y1="1" x2="1" y2="0">
      <stop offset="0" stop-color="#2a1a16" stop-opacity=".35"/>
      <stop offset=".5" stop-color="#2a1a16" stop-opacity="0"/>
      <stop offset="1" stop-color="#2a1a16" stop-opacity=".25"/>
    </linearGradient>
    <g id="card-art">
      <rect width="760" height="434" fill="url(#base)"/>
      <polygon points="300,434 520,0 620,0 420,434" fill="url(#band)"/>
      <polygon points="180,160 760,300 760,380 150,230" fill="url(#band)" opacity=".75"/>
      <polygon points="0,0 470,0 760,150 760,210 220,120" fill="url(#haze)"/>
      <polygon points="120,434 330,200 360,230 200,434" fill="#4a3230" opacity=".35"/>
      <rect width="760" height="434" fill="url(#strands)" role="img" aria-label="Fine hair strands drawn across the card"/>
      <path d="M0 0 H430 C380 60 300 40 250 110 C200 170 120 190 60 260 C40 290 20 300 0 310 Z" fill="url(#ink)" role="img" aria-label="Dark ink splash texture"/>
    </g>
    <g id="ico-phone">
      <circle cx="9" cy="9" r="8.5" fill="#d9a24a"/>
      <path d="M6 4.5 l2 2 -1 1.3 a6 6 0 0 0 3.2 3.2 l1.3 -1 2 2 -1.2 1.5 C8.5 13.2 4.8 9.5 4.5 5.7 Z" fill="#3a2620"/>
    </g>
    <g id="ico-mail">
      <circle cx="9" cy="9" r="8.5" fill="#d9a24a"/>
      <rect x="4.5" y="6" width="9" height="6.5" fill="none" stroke="#3a2620" stroke-width="1.2"/>
      <path d="M4.5 6 L9 9.8 L13.5 6" fill="none" stroke="#3a2620" stroke-width="1.2"/>
    </g>
    <g id="ico-web">
      <circle cx="9" cy="9" r="8.5" fill="#d9a24a"/>
      <circle cx="9" cy="9" r="4.5" fill="none" stroke="#3a2620" stroke-width="1.2"/>
      <path d="M4.5 9 H13.5 M9 4.5 V13.5" stroke="#3a2620" stroke-width="1"/>
    </g>
  </defs>
</svg>

<section class="card card--intro">
  <svg class="card__art" viewBox="0 0 760 434" aria-hidden="true"><use href="#card-art"/></svg>
  <div class="brand brand--cosmetics">
    <span class="brand__mark"></span>
    <span class="brand__name">Velmora Cosmetics</span>
  </div>
  <p class="role">Tobin Carlyle Independent Distributor</p>
  <div class="icon-row">
    <svg viewBox="0 0 18 18"><use href="#ico-phone"/></svg>
    <svg viewBox="0 0 18 18"><use href="#ico-mail"/></svg>
  </div>
  <div class="brand brand--jewellery">
    <span class="brand__mark"></span>
    <span class="brand__name">Velmora Designer Jewellery</span>
  </div>
</section>

<section class="card card--contact">
  <svg class="card__art" viewBox="0 0 760 434" aria-hidden="true"><use href="#card-art"/></svg>
  <p class="brand__tagline">independent distributor for</p>
  <div class="brand brand--cosmetics">
    <span class="brand__mark"></span>
    <span class="brand__name">Velmora Cosmetics</span>
  </div>
  <p class="role">Tobin Carlyle Independent Distributor</p>
  <ul class="contact-list">
    <li><svg viewBox="0 0 18 18"><use href="#ico-phone"/></svg>0483 259 470</li>
    <li><svg viewBox="0 0 18 18"><use href="#ico-mail"/></svg>tobin@quorvel.org</li>
    <li><svg viewBox="0 0 18 18"><use href="#ico-web"/></svg>Product info &amp; online orders</li>
  </ul>
  <div class="brand brand--jewellery">
    <span class="brand__mark"></span>
    <span class="brand__name">Velmora Designer Jewellery</span>
  </div>
  <p class="side-line">Distributor ID: 384752<br>www.velmoracosmetics-example.com.au/tobincarlyle</p>
</section>

</body>
</html>
```